Desing for real estate offers- Package system

The word should be graphically clear and understandable. There are 3 packages that the customer can buy: the basic package is red, the medicinal package is green and the carefree package is blue. See the Word document in the appendix. End file should be a Word, as we need to chance the text. It should also match the website as well as the business card.
https://brelunor.vantosite.ch/
Colors:
Green 1: R: 187, G: 214, B: 49
Green 2: R: 119, G: 187, W: 66

Target Market(s)

Real estate company

Font styles to use
Serif
Sans Serif

```html
<!DOCTYPE html>
<html lang="de">
<head>
<meta charset="utf-8">
<title>Brelunor – Verkaufspakete</title>
<link href="https://fonts.googleapis.com/css2?family=Barlow:ital,wght@0,400;0,500;0,600;1,500&family=Archivo+Black&family=Arimo&display=swap" rel="stylesheet">
<style>
  :root{
    --green-1:#bbd631;
    --green-2:#77bb42;
    --head-green:#a6d494;
    --box-green:#e2f0d9;
    --ink:#1c1c1c;
    --page-bg:#b3b3b3;
    --photo-a:#d9d2c8;
    --photo-b:#6b5a4c;
    --photo-c:#2c3648;
  }
  *{box-sizing:border-box;margin:0;padding:0}
  html,body{width:1200px;height:1200px;overflow:hidden;background:var(--page-bg)}
  .sheet{
    position:absolute;left:190px;top:20px;width:820px;height:1160px;
    background:linear-gradient(90deg,var(--green-1) 0%,var(--green-1) 50%,var(--green-2) 50%,var(--green-2) 100%);
  }
  .page{
    position:absolute;left:23px;top:14px;right:27px;bottom:15px;background:#fff;
    font-family:"Barlow",Arial,sans-serif;color:var(--ink);
  }
  .sheet > *:not(.page){position:absolute}
  .brand{
    position:absolute;left:583px;top:34px;font-family:"Barlow",sans-serif;font-weight:600;
    font-size:29px;color:var(--green-1);letter-spacing:.3px;
  }
  .prices{position:absolute;left:0;right:0;top:87px;text-align:center;font-size:15.5px;font-weight:500}
  .prices p{line-height:32px}
  .note{
    position:absolute;left:40px;right:40px;top:195px;text-align:center;
    font-size:13.5px;font-style:italic;font-weight:500;line-height:19px;
  }
  .photo{
    position:absolute;left:1px;top:241px;width:772px;height:279px;
    background:linear-gradient(100deg,var(--photo-a) 0%,#c9bfb2 30%,var(--photo-b) 60%,var(--photo-c) 85%,#5a4233 100%);
  }
  .photo-tag{
    position:absolute;left:627px;top:453px;width:135px;height:55px;background:#fff;
    display:flex;align-items:center;justify-content:center;text-align:center;
    font-style:italic;font-weight:500;font-size:14px;line-height:19px;
  }
  .pkg-title{
    position:absolute;font-family:"Archivo Black","Arial Black",sans-serif;
    font-size:49px;line-height:40px;color:var(--head-green);letter-spacing:.5px;
  }
  .box{position:absolute;background:var(--box-green);font-size:13.3px;font-weight:500;line-height:19.3px}
  .box ul{list-style:none}
  .box li{position:relative}
  .box li::before{content:"";position:absolute;width:4px;height:4px;border-radius:50%;background:var(--ink)}
  .box-basis{left:10px;top:615px;width:262px;height:414px;padding:12px 10px 0 47px}
  .box-basis li::before{left:-22px;top:8px}
  .box-medicinal{left:284px;top:615px;width:464px;height:127px;padding:12px 10px 0 24px}
  .box-carefree{left:284px;top:793px;width:464px;height:236px;padding:12px 10px 0 11px}
  .box-medicinal ul,.box-carefree ul{margin-top:11px;padding-left:13px}
  .box-carefree ul{padding-left:26px}
  .box-medicinal li::before,.box-carefree li::before{left:-10px;top:8px}
  .title-basis{left:9px;top:580px}
  .title-medicinal{left:282px;top:580px}
  .title-carefree{left:283px;top:757px}
  .contact{position:absolute;left:516px;top:1062px;font-family:"Arimo",Arial,sans-serif;font-size:14.5px;line-height:19.6px}
  .contact li{list-style:none;display:flex;align-items:center;gap:6px}
  .contact svg{width:13px;height:13px;flex:none}
</style>
</head>
<body>
<div class="sheet">
  <div class="page">
    <div class="brand">Brelunor</div>
    <div class="prices">
      <p>Basis-Paket 8'500.- CHF exkl. MWST</p>
      <p>Medium-Paket 10'900 CHF exkl. MWST</p>
      <p>Sorglos: 2% vom Verkaufspreis inkl. MWST (von Grundstückgewinnsteuer abziehbar)</p>
    </div>
    <p class="note">Unterlagen müssen gestellt werden, ansonsten werden Sie 1:1 verrechnet: GB-Auszug,GVZ,<br>Nebenkostenabrechnung, STWEG-Protokolle der letzten 3 Jahren, …</p>

    <div class="photo" role="img" aria-label="Foto: Handschlag zweier Personen über einem kleinen Holzhausmodell"></div>
    <div class="photo-tag">Temporary<br>Picture</div>

    <div class="box box-basis">
      <ul>
        <li>Begehung Verkaufsobjekt</li>
        <li>Hedonische Schätzung intern &amp; Bank</li>
        <li>Marketing &amp; Vertriebskonzept</li>
        <li>Unterlagen einfordern- STWEG Protokolle, GB Auszug u.s.w wenn nötig</li>
        <li>Fotografieren &amp; Ausmessen der Immobilie</li>
        <li>Grundriss zeichnen</li>
        <li>Dokumentation erstellen</li>
        <li>Immobilie Online aufbereiten &amp; Aufschalten</li>
        <li>Interessenten &amp; Kaufangebote prüfen</li>
        <li>Käufer zusage- andere noch vertrösten</li>
        <li>Erstellung erster Kaufvertragsentwurf</li>
      </ul>
    </div>
    <div class="pkg-title title-basis">BASIS</div>

    <div class="box box-medicinal">
      <p>Basis Paket +</p>
      <ul>
        <li>Unsere Interessenten anschreiben</li>
        <li>Anfragen beantworten- telefonisch &amp; elektronisch</li>
        <li>Evt. Bieterverfahren modern oder altmodisch</li>
        <li>Begleitung aufs Notariat</li>
      </ul>
    </div>
    <div class="pkg-title title-medicinal">MEDICINAL</div>

    <div class="box box-carefree">
      <p>Medicinal Paket +</p>
      <ul>
        <li>Besichtigungen koordinieren</li>
        <li>Besichtigungen Durchführen</li>
        <li>Sicherheitsnachweis (SINA)- organisieren</li>
        <li>Erstellung erster Kaufvertragsentwurf</li>
        <li>Berechnung provisorische Grundstückgewinnsteuer- Steueramt</li>
        <li>Beurkundungstermin vereinbaren</li>
        <li>Eigentumsübertragung vereinbaren</li>
        <li>Helfen bei der Steuererklärung für die definitive Grundstückgewinnsteuer</li>
      </ul>
    </div>
    <div class="pkg-title title-carefree">CAREFREE</div>

    <ul class="contact">
      <li><svg viewBox="0 0 14 14"><circle cx="7" cy="7" r="7" fill="#77bb42"/><path d="M4.3 3.6l1.4-.2.7 1.7-.8.6c.4.9 1.1 1.6 2 2l.6-.8 1.7.7-.2 1.4C6.9 9.2 4.6 6.9 4.3 3.6z" fill="#fff"/></svg>044 310 27 64</li>
      <li><svg viewBox="0 0 14 14"><circle cx="7" cy="7" r="7" fill="#77bb42"/><rect x="3.5" y="4.5" width="7" height="5" rx=".6" fill="#fff"/><path d="M3.7 4.8L7 7.3l3.3-2.5" stroke="#77bb42" stroke-width=".8" fill="none"/></svg>lena.moser@brelunor.ch</li>
      <li><svg viewBox="0 0 14 14"><circle cx="7" cy="7" r="7" fill="#77bb42"/><circle cx="7" cy="7" r="3.6" fill="none" stroke="#fff" stroke-width=".9"/><path d="M3.4 7h7.2M7 3.4c-1.4 2-1.4 5.2 0 7.2M7 3.4c1.4 2 1.4 5.2 0 7.2" stroke="#fff" stroke-width=".8" fill="none"/></svg>brelunor.vantosite.ch</li>
    </ul>
  </div>
</div>
</body>
</html>
```